South Florida Real Estate Brokerage Business

The name is DWELL VANTORO REAL ESTATE.
The company is a Real estate realty based in Miami.
Is targeted to Latin American clients.
Must express luxury, and efficiency.
Target clients for properties around 250k to a million +.
Vantoro means Royal in Latin.
Should communicate safety and knowledge of the product and transaction with a tech edge.

The web design needs to be a Social tool, with Chatterloop and other media integration of some sort. Needs to have a Show case place, a Search place (MLS listings) with maps and filters.
Needs to reflect luxury but also mixed with a social edge capable of engaging clients or transition them to communicate with the page.
Include the logo from the uploaded files, feel free to change the color or font per webdesign.
This is a Front en design, layout and graphics.
Possible future programming if approved.
I can receive Quotes for the Code part.

Target Market(s)

Spanish and English speakers living in Latin America and Canada looking for apartments and houses to buy.

Industry/Entity Type

Business

Requirements
Must have
• Search area.
Neighbourhood area.
Could be a blog or news area.
Client registration.
Social Plugin
Nice to have
• Social linking to networks.
Log in with chatterloop account.
Chatterloop Like.

```html
<!DOCTYPE html>
<html lang="en">
<head>
<meta charset="utf-8">
<title>Dwell Vantoro Real Estate</title>
<link href="https://fonts.googleapis.com/css2?family=PT+Sans:wght@400;700&family=Oswald:wght@500&display=swap" rel="stylesheet">
<style>
:root{
  --gold:#c9a45c;
  --gold-dark:#a9823a;
  --gold-light:#e3c88a;
  --band:#c69a55;
  --panel:#1f1f1f;
  --footer:#2a2a2a;
  --ink:#222;
  --muted:#555;
  --orange:#f6a623;
  --orange-dark:#e8901a;
  --sky-top:#4f9ae3;
  --sky-low:#a9d2f2;
  --grass:#5f9a3a;
  --white:#fff;
}
*{box-sizing:border-box;margin:0;padding:0}
html,body{width:1200px;height:1044px;overflow:hidden}
body{position:relative;font-family:"PT Sans",Arial,sans-serif;color:var(--ink);background:var(--band)}
.abs{position:absolute}
.hero{left:0;top:0;width:1200px;height:802px;
  background:linear-gradient(180deg,var(--sky-top) 0%,var(--sky-low) 42%,#8fb7a4 58%,#7b8f7a 66%,var(--grass) 82%,#4f8a30 100%)}

/* search panel */
.search-panel{left:150px;top:0;width:226px;height:474px}
.search-panel svg{position:absolute;left:0;top:0}
.brand{position:absolute;left:0;top:18px;width:226px;text-align:center;color:var(--gold)}
.brand-mark{display:block;width:38px;height:38px;margin:0 auto 10px;border:2px solid var(--gold)}
.brand-name{font-size:22px;line-height:26px;font-weight:400;letter-spacing:1px}
.brand-sub{font-size:15px;letter-spacing:2px;font-weight:400}
.search-title{position:absolute;left:22px;top:160px;font-size:21px;color:var(--gold);text-transform:uppercase;white-space:nowrap}
.field-label{position:absolute;font-size:14px;color:var(--gold-light)}
.field{position:absolute;height:23px;background:var(--white);border:1px solid #bbb;font-size:12px;color:#777;padding:4px 8px}
.field.select::after{content:"";position:absolute;right:0;top:0;width:22px;height:21px;background:var(--gold)}
.field.select::before{content:"";position:absolute;right:6px;top:8px;border:5px solid transparent;border-top-color:var(--white);z-index:1}
.field-to{position:absolute;font-size:12px;color:var(--gold-light)}
.btn-gold{position:absolute;height:30px;border-radius:5px;border:1px solid var(--gold-dark);
  background:linear-gradient(180deg,#e9d09a,#b98a3e);color:var(--white);font-weight:700;font-size:14px;text-align:center;line-height:28px}
.adv-link{position:absolute;left:0;width:226px;top:436px;text-align:center;font-size:12px;color:#b98a3e;font-weight:700}

/* header right */
.login-title{left:694px;top:14px;font-size:14px;color:#111;text-transform:uppercase}
.input{background:var(--white);border:1px solid #ccc;font-size:12px;color:#333;padding:3px 6px;height:23px;white-space:nowrap;overflow:hidden}
.btn-light{background:linear-gradient(180deg,#fafafa,#d8d8d8);border:1px solid #bbb;border-radius:5px;font-size:13px;text-align:center;line-height:21px;color:#333}
.forgot{left:696px;top:62px;font-size:12px;color:#111}
.search-strip{left:694px;top:92px;width:367px;height:33px;background:rgba(255,255,255,.85)}
.nav{left:386px;top:125px;width:675px;height:38px;background:var(--white);display:flex;align-items:center;justify-content:space-between;padding:0 18px 0 26px;box-shadow:0 3px 6px rgba(0,0,0,.25)}
.nav span{font-size:14px;color:#111;white-space:nowrap;text-transform:uppercase}

/* showcase thumbs */
.showcase{left:888px;top:200px;width:164px;height:390px;background:rgba(255,255,255,.35)}
.thumb{position:absolute;left:12px;width:140px;height:80px;border:3px solid var(--white)}
.thumb.active{border-color:#111;left:11px}
.pointer{left:876px;top:242px;border:8px solid transparent;border-right-color:rgba(255,255,255,.6)}

/* content boxes */
.content{left:140px;top:632px;width:921px;height:200px;display:flex;box-shadow:0 2px 6px rgba(0,0,0,.3)}
.box{position:relative;height:200px;background:#f2f2f2;overflow:hidden}
.box h2{height:42px;line-height:42px;padding-left:22px;font-size:15px;font-weight:700;text-transform:uppercase;white-space:nowrap;
  background:linear-gradient(180deg,#fff,#e3e3e3);border-bottom:1px solid #ccc}
.box p{font-size:12px;line-height:17px;color:var(--muted)}
.welcome{width:389px;border-right:1px solid #ccc}
.welcome p{padding:14px 14px 0 22px}
.news{width:233px;border-right:1px solid #ccc}
.news .headline{padding:9px 8px 0 17px;color:#b98a3e}
.news p.body{padding:7px 8px 0 17px;font-size:11.5px;line-height:16px}
.news .more{padding:6px 0 0 17px;color:#b98a3e}
.hood{width:299px;background:linear-gradient(180deg,var(--orange),var(--orange-dark))}
.hood h2{background:linear-gradient(180deg,#fcc04a,#f4a21e);border-bottom:1px solid #dd8a10;color:#2a1a00}
.hood .map{position:absolute;left:6px;top:58px;width:160px;height:108px;border-radius:12px 30px 20px 40px;background:#f2dfae}
.hood p{position:absolute;left:170px;top:56px;width:122px;color:var(--white);font-size:12px;line-height:17px}

/* footer band */
.col-title{font-size:16px;color:#222}
.qlinks a{position:absolute;font-size:12px;color:var(--white);text-decoration:none}
.mail-title{left:373px;top:849px;background:#111;color:var(--white);font-family:"Oswald",sans-serif;font-size:22px;line-height:30px;padding:0 3px;text-transform:uppercase}
.mail-text{left:373px;top:890px;width:170px;font-size:13px;line-height:17px;color:#222}
.mail-input{left:372px;top:940px;width:202px;height:24px;border-radius:12px;background:var(--white);font-size:12px;color:#333;padding:4px 10px}
.mail-join{left:537px;top:940px;width:38px;height:24px;border-radius:12px;background:#ef7a1c;color:var(--white);font-size:12px;font-weight:700;text-align:center;line-height:24px;text-transform:uppercase}
.blog-date{font-size:11px;color:#fff;letter-spacing:1px;font-weight:700}
.blog-post{font-size:12px;line-height:16px;color:#fff;font-weight:700;width:240px}
.social{display:flex;align-items:center;gap:4px;font-size:11px;color:#222;font-weight:700;white-space:nowrap}
.social i{display:block;width:14px;height:14px;background:#2b4f86}
.pill{background:#f4f4f4;border:1px solid #bbb;border-radius:3px;font-size:11px;padding:1px 5px;color:#333}
.likes{font-size:11px;color:#fff}

.base{left:0;top:984px;width:1200px;height:60px;background:var(--footer)}
.base-brand{left:126px;top:990px;width:90px;text-align:center;color:var(--gold);font-size:9px;line-height:10px;white-space:nowrap}
.base-brand i{display:block;width:14px;height:14px;border:1px solid var(--gold);margin:0 auto 3px}
.copy{left:226px;top:1019px;font-size:12px;color:#eee}
</style>
</head>
<body>

<div class="abs hero" role="img" aria-label="Photograph of a large two-storey family house with porch, lawn and blue sky"></div>

<div class="abs search-panel">
  <svg width="226" height="474" viewBox="0 0 226 474">
    <path d="M0 0H226V440Q113 400 0 440Z" fill="#1f1f1f"/>
    <path d="M0 440Q113 408 226 440" stroke="#c9a45c" stroke-width="2" fill="none"/>
    <line x1="10" y1="124" x2="216" y2="124" stroke="#c9a45c" stroke-width="1"/>
  </svg>
  <div class="brand">
    <span class="brand-mark"></span>
    <div class="brand-name">DWELL VANTORO</div>
    <div class="brand-sub">REAL ESTATE</div>
  </div>
  <div class="search-title">Propertyes Search</div>
  <div class="field-label" style="left:20px;top:192px">City</div>
  <div class="field" style="left:20px;top:210px;width:188px"></div>
  <div class="field-label" style="left:17px;top:239px">Location</div>
  <div class="field select" style="left:17px;top:257px;width:190px">Any</div>
  <div class="field-label" style="left:17px;top:286px">Price</div>
  <div class="field select" style="left:17px;top:304px;width:88px">Any</div>
  <div class="field-to" style="left:109px;top:310px">to</div>
  <div class="field select" style="left:122px;top:304px;width:85px">Any</div>
  <div class="field-label" style="left:17px;top:333px">Beds</div>
  <div class="field select" style="left:17px;top:351px;width:88px">Any</div>
  <div class="field-to" style="left:109px;top:357px">to</div>
  <div class="field-label" style="left:122px;top:333px">Baths</div>
  <div class="field select" style="left:122px;top:351px;width:85px">Any</div>
  <div class="btn-gold" style="left:17px;top:394px;width:190px">PROPERTY SEARCH</div>
  <div class="adv-link">Advanced Search</div>
</div>
<div class="btn-gold" style="left:168px;top:486px;width:188px">SEARCH BY MLS #</div>

<div class="abs login-title">Client Login</div>
<div class="abs input" style="left:694px;top:36px;width:152px">Username</div>
<div class="abs input" style="left:852px;top:36px;width:150px">Password</div>
<div class="abs btn-light" style="left:1008px;top:35px;width:53px;height:24px">LOGIN</div>
<div class="abs forgot">Forgot your password? / Register</div>
<div class="abs search-strip"></div>
<div class="abs input" style="left:702px;top:97px;width:320px;height:24px;color:#777;font-size:11px">MLS ID, Building Name, Address, City, Zip, or Agent Name</div>
<div class="abs btn-light" style="left:1026px;top:97px;width:30px;height:24px">GO</div>
<nav class="abs nav">
  <span>Home</span><span>Company</span><span>Associates</span><span>Search Properties</span><span>Marketing and Design</span><span>Contact</span>
</nav>

<div class="abs pointer"></div>
<div class="abs showcase">
  <div class="thumb active" role="img" aria-label="Showcase photo of a blue two-storey house" style="top:11px;width:142px;background:linear-gradient(180deg,#4a8ad6,#8aa4c0 55%,#5d8a3c)"></div>
  <div class="thumb" role="img" aria-label="Showcase photo of a waterfront villa with palm trees" style="top:109px;background:linear-gradient(180deg,#6aa7e6,#c9a26a 55%,#3f8fb0)"></div>
  <div class="thumb" role="img" aria-label="Showcase photo of a Mediterranean style home" style="top:205px;background:linear-gradient(180deg,#7ab0e8,#c8a48a 55%,#6d8a50)"></div>
  <div class="thumb" role="img" aria-label="Showcase photo of a house with white porch" style="top:302px;background:linear-gradient(180deg,#9cc4ec,#5a6e72 45%,#e6e6e0 75%,#5e8a3a)"></div>
</div>

<section class="abs content">
  <article class="box welcome">
    <h2>Welcome to Dwell Vantoro Real Estate</h2>
    <p>Lorem ipsum dolor sit amet, consectetur adipisicing elit, sed do eiusmod tempor incididunt ut labore et dolore magna aliqua. Ut enim ad minim veniam, quis nostrud exercitation ullamco laboris nisi ut aliquip ex ea commodo consequat. Duis aute irure dolor in reprehenderit in voluptate velit esse cillum dolore eu fugiat nulla pariatur. Excepteur sint occaecat cupidatat non proident, sunt in culpa qui officia deserunt mollit anim id est laborum.</p>
  </article>
  <article class="box news">
    <h2>News</h2>
    <p class="headline">Lorem ipsum dolor sit amet</p>
    <p class="body">Lorem ipsum dolor sit amet, consectetur adipisicing elit, sed do eiusmod tempor incididunt ut labore et dolore magna aliqua. Ut enim ad minim veniam, quis nostrud exercitation ullamco laboris.</p>
    <p class="more">Read more...</p>
  </article>
  <article class="box hood">
    <h2>Neighbourhood Area</h2>
    <div class="map" role="img" aria-label="Map of the United States highlighting service areas"></div>
    <p>Lorem ipsum dolor sit amet, consectetur adipisicing elit, sed do eiusmod tempor incididunt ut labore et dolore magna aliqua.</p>
  </article>
</section>

<div class="abs col-title" style="left:140px;top:847px">Quick Links</div>
<div class="qlinks">
  <a style="left:144px;top:876px">Home</a>
  <a style="left:144px;top:899px">About Us</a>
  <a style="left:144px;top:922px">Search Properties</a>
  <a style="left:144px;top:945px">News</a>
  <a style="left:271px;top:876px">BLog</a>
  <a style="left:271px;top:899px">Testimonials</a>
  <a style="left:271px;top:922px">Contact</a>
</div>

<div class="abs mail-title">Join our mailing list</div>
<div class="abs mail-text">Sign up for our e-mail list to receive updates</div>
<div class="abs mail-input">Your e-mail address</div>
<div class="abs mail-join">Join</div>

<div class="abs col-title" style="left:625px;top:847px">Blog</div>
<div class="abs blog-date" style="left:626px;top:870px">09 April 2012</div>
<div class="abs blog-post" style="left:626px;top:885px">Lorem ipsum dolor sit amet, consectetur adipisicing elit, sed do</div>
<div class="abs blog-date" style="left:626px;top:924px">06 April 2012</div>
<div class="abs blog-post" style="left:626px;top:939px">Lorem ipsum dolor sit amet, consectetur adipisicing elit, sed do</div>

<div class="abs col-title" style="left:871px;top:847px">Connect With Us</div>
<div class="abs social" style="left:874px;top:880px"><i></i>Chatterloop</div>
<div class="abs social" style="left:970px;top:880px"><i></i>Chirpwave</div>
<div class="abs social" style="left:874px;top:900px"><i></i>Linkora</div>
<div class="abs social" style="left:970px;top:900px"><i style="background:#e67a1c"></i>Feedline</div>
<div class="abs social" style="left:876px;top:918px"><span class="pill">Plusmark</span><span class="pill">17</span></div>
<div class="abs social" style="left:876px;top:946px"><span class="pill">Like</span><span class="likes">Chatterloop · 2,942 people like this.</span></div>

<div class="abs base"></div>
<div class="abs base-brand"><i></i>DWELL VANTORO<br>REAL ESTATE</div>
<div class="abs copy">© 2011 Dwell Vantoro Real Estate .All Rights Reserved</div>

</body>
</html>
```